Corrimal Lodge Web Design Project

I am looking for a striking, modern and user friendly site to promote my business, Corrimal Lodge.

Corrimal Lodge comprises of 3 elements : Restaurant, Resort and Events and the site must showcase all of these.
Updates

Project Deadline Extended
Reason: Too far away from brief ! Please check out the 2 website links to restaurant sites i LOVE for inspiration ! I am happy to pay for a quality designer and also for anyone that can code this !

Target Market(s)

Our Restaurant clientele demographic is 30-60 years old and are a mix of locals and tourists. The Restaurant is very much a destination venue so we attract people that wish to seek out amazing food.

The Event side of things attracts mainly weddings, this is a lucrative arm of the business and this side of the site must also be outstanding.

The Resort comprises of 7 boutique loft apartment and has a big pool and spa. We attract a mix of locals but want to push it as a ' getaway '

Industry/Entity Type

Business

Requirements
Must have
• I would like the first page to be an overall blog and to highlight the 3 area of the business. Lets have the 3 keywords as clickable tabs that take you to that section of the site.

RESTAURANT RESORT EVENTS

The RESTAURANT page should include the following tabs ( i have provided the information to be added to each tab as an example )

MENU ( Breakfast, Lunch, Dinner, Set Menu, Wine List)

FUNCTIONS (Private Dining Room, Exclusive Use, Wine Nights Coming Soon)

RESERVATIONS (Enquiry Form linked to my info@ address, Reservation Policies, Contact Number)

GALLERY & PRESS ( Press Articles, Latest News, What's On, Photo's, Wedding Hot Spot)

CONTACT US (Opening Times, Map, Contact Details, Sign Up For Our Newsletter, Facebook Link )

The RESORT page should include the following tabs :
# LOFTS & RATES
# FACILITIES
# SPECIAL OFFERS
# GALLERY
# RESERVATIONS

The EVENTS page should include the following tabs :
# WEDDINGS
# CONFERENCES
# PRIVATE EVENTS
# GALLERY
# ENQUIRY FORM
Nice to have
• Include Logo, good branding

```html
<!DOCTYPE html>
<html lang="en">
<head>
<meta charset="utf-8">
<title>Corrimal Lodge — Restaurant, Resort, Events</title>
<link href="https://fonts.googleapis.com/css2?family=Arimo:wght@400;700&family=Dancing+Script&display=swap" rel="stylesheet">
<style>
  :root{
    --page:#f4f4f6;
    --ink:#222222;
    --ink-soft:#333333;
    --muted:#b4b4b8;
    --faint:#d6d6da;
    --accent:#9cbb1e;
    --sun:#f5a800;
    --panel:#f8f8fa;
    --panel-hi:#fbfbfc;
    --white:#ffffff;
  }
  *{box-sizing:border-box;margin:0;padding:0}
  html,body{width:882px;height:1200px;overflow:hidden;background:var(--page)}
  body{position:relative;font-family:"Arimo",Arial,sans-serif;color:var(--ink)}

  .search{position:absolute;left:658px;top:78px;width:95px;height:22px;border:1px solid var(--faint);background:var(--panel-hi);box-shadow:0 2px 3px rgba(0,0,0,.06);font-size:10px;color:var(--faint);text-align:center;line-height:21px}
  .search-btn{position:absolute;left:765px;top:79px;width:20px;height:20px;border-radius:50%;background:var(--panel-hi);box-shadow:0 2px 3px rgba(0,0,0,.12)}
  .search-btn svg{display:block;margin:4px}

  .brand{position:absolute;left:0;width:882px;top:302px;text-align:center;white-space:nowrap}
  .brand-name{font-size:13px;color:var(--ink);display:flex;align-items:center;justify-content:center;gap:6px}
  .brand-name::before{content:"";width:9px;height:9px;background:var(--ink)}
  .brand-tag{font-size:6px;font-weight:700;margin-top:2px;letter-spacing:.2px}
  .brand-glow{position:absolute;left:259px;top:352px;width:384px;height:2px;background:radial-gradient(ellipse at center,rgba(0,0,0,.08),rgba(0,0,0,0) 70%)}

  .since{position:absolute;left:0;width:882px;top:370px;text-align:center;font-weight:700;color:var(--accent);font-size:10px;white-space:nowrap}
  .since b{font-size:19px;color:var(--ink-soft);margin:0 4px;vertical-align:-2px}

  .showcase{position:absolute;left:0;top:420px;width:882px;height:202px;overflow:hidden}
  .photo{position:absolute;border-radius:50%;border:14px solid var(--white);box-shadow:0 0 10px rgba(0,0,0,.08)}
  .photo-food{left:196px;top:35px;width:224px;height:224px;background:radial-gradient(circle at 45% 55%,#c4612c,#7a3a1c 55%,#3c2616)}
  .photo-events{left:489px;top:64px;width:224px;height:224px;background:radial-gradient(circle at 45% 35%,#e7f6b5,#8fc432 40%,#234a12 80%)}
  .photo-resort{left:326px;top:14px;width:232px;height:232px;background:radial-gradient(circle at 60% 60%,#f3f1ea,#cfd3c0 40%,#56692c 85%)}

  .tabs{position:absolute;left:93px;top:622px;width:695px;height:94px;display:flex;gap:3px}
  .tab{flex:0 0 auto;display:flex;align-items:center;justify-content:center;gap:14px;background:var(--panel);text-decoration:none;color:var(--ink-soft);white-space:nowrap}
  .tab-food{width:228px}
  .tab-resort{width:242px;background:var(--panel-hi);box-shadow:0 0 8px rgba(0,0,0,.1)}
  .tab-events{width:220px}
  .tab-label{line-height:1}
  .tab-kicker{display:block;font-size:10px;font-weight:700;color:var(--accent);margin-bottom:3px}
  .tab-title{display:block;font-size:17px;font-weight:700}
  .tab-resort .tab-label{text-align:center}
  .tab-resort .tab-kicker{margin:2px 0 0;font-size:8px}
  .tab-events .tab-label{text-align:right}

  .greeting{position:absolute;left:0;width:882px;top:796px;text-align:center;font-size:33px;font-weight:700;color:var(--ink)}
  .welcome{position:absolute;left:359px;top:851px;width:197px;height:78px;border-top:1px solid var(--faint);border-bottom:1px solid var(--faint)}
  .welcome p{position:absolute;left:23px;font-size:13px;line-height:15px;color:var(--muted);white-space:nowrap}
  .welcome .l1{top:15px}
  .welcome .l2{top:41px}
  .smile{position:absolute;left:551px;top:884px;font-size:19px;color:var(--accent)}
  .signoff{position:absolute;left:561px;top:915px;font-family:"Dancing Script",cursive;font-size:12px;color:#8a8a8e;white-space:nowrap}
</style>
</head>
<body>
  <div class="search">search</div>
  <div class="search-btn"><svg width="12" height="12" viewBox="0 0 12 12"><circle cx="4.5" cy="4.5" r="3" fill="none" stroke="#666" stroke-width="1.4"/><path d="M6.8 6.8 10.5 10.5" stroke="#666" stroke-width="1.8"/></svg></div>

  <header class="brand">
    <div class="brand-name">Corrimal Lodge</div>
    <div class="brand-tag">restaurant - resort - events</div>
  </header>
  <div class="brand-glow"></div>

  <div class="since">SINCE <b>60</b> YEARS</div>

  <section class="showcase">
    <div class="photo photo-food" role="img" aria-label="Restaurant table with pizza and fresh tomatoes"></div>
    <div class="photo photo-events" role="img" aria-label="Concert crowd under green stage lights"></div>
    <div class="photo photo-resort" role="img" aria-label="Guest relaxing beside a flower and cool drink at the resort"></div>
  </section>

  <nav class="tabs">
    <a class="tab tab-food" href="#restaurant">
      <svg width="48" height="44" viewBox="0 0 48 44">
        <path d="M22 4c3 2-3 4 0 6s-2 4 0 6" fill="none" stroke="#999" stroke-width="1"/>
        <circle cx="24" cy="20" r="2" fill="none" stroke="#333"/>
        <path d="M8 34a16 13 0 0 1 32 0z" fill="#fff" stroke="#333" stroke-width="1.2"/>
        <ellipse cx="24" cy="36" rx="21" ry="3" fill="#fff" stroke="#333" stroke-width="1.2"/>
      </svg>
      <span class="tab-label"><span class="tab-kicker">ENJOY FOOD</span><span class="tab-title">RESTURANT</span></span>
    </a>
    <a class="tab tab-resort" href="#resort">
      <svg width="52" height="50" viewBox="0 0 52 50">
        <g stroke="#f5a800" stroke-width="2">
          <path d="M38 2v5M38 27v-5M26 14.5h5M50 14.5h-5M29.5 6l3.5 3.5M46.5 23l-3.5-3.5M29.5 23l3.5-3.5M46.5 6l-3.5 3.5"/>
        </g>
        <circle cx="38" cy="14.5" r="7" fill="#f5a800"/>
        <path d="M3 29l12 13h30M22 42l-7 7M42 42l5 7" fill="none" stroke="#555" stroke-width="4" stroke-linecap="round"/>
      </svg>
      <span class="tab-label"><span class="tab-title">RESORT</span><span class="tab-kicker">ENJOY TIMES</span></span>
    </a>
    <a class="tab tab-events" href="#events">
      <svg width="56" height="50" viewBox="0 0 56 50">
        <path d="M40 34l14 13-4 2-14-11z" fill="#222"/>
        <g fill="none" stroke="#f5a800" stroke-width="1.6" stroke-linecap="round">
          <path d="M36 30C30 20 22 14 10 12M38 28c0-10 2-16 8-22M34 32C24 28 14 30 6 36M32 26c-4-6-8-10-12-20"/>
        </g>
        <g fill="#f5a800">
          <circle cx="6" cy="20" r="1.5"/><circle cx="16" cy="4" r="1.5"/><circle cx="28" cy="3" r="1.2"/><circle cx="3" cy="30" r="1.2"/><circle cx="48" cy="14" r="1.5"/><circle cx="14" cy="42" r="1.2"/>
        </g>
      </svg>
      <span class="tab-label"><span class="tab-kicker">ENJOY TIME</span><span class="tab-title">EVENTS</span></span>
    </a>
  </nav>

  <h1 class="greeting">HI</h1>
  <div class="welcome">
    <p class="l1">WELCOME TO OUR WEBSITE</p>
    <p class="l2">ENJOY YOUR JOURNEY</p>
  </div>
  <div class="smile">:)</div>
  <div class="signoff">Corrimal Lodge</div>
</body>
</html>
```